Neuropsychology Private Practice - Advertising Materials

We need a postcard (probably multiple) to let other doctors in the area know about our private practice, what we have to offer, and where we are at. This would be something to hand out to Dr.'s and also leave in their waiting rooms. Much more through information about the types of services offered at the practice and what a neuropsychological assessment is are included in the supplemental (attacked documents). Also there is a digital copy of the practices logo

Target Market(s)

Medical Professionals (MD's, Nurse Practitioners, OT/PT).

Industry/Entity Type

Advertising

Font styles to use
Serif
Sans Serif

Requirements
Must have
• Practice Logo, Contact Information, Provider Information
Nice to have
• Images, Pictures, something to catch a person's eye

```html
<!DOCTYPE html>
<html lang="en">
<head>
<meta charset="utf-8">
<title>Harbor Family Wellness Clinic – Practice Flyers</title>
<link rel="stylesheet" href="https://fonts.googleapis.com/css2?family=Lato:wght@300;400;700&display=swap">
<style>
  :root{
    --backdrop:#e9e6e1;
    --paper:#ffffff;
    --paper-tint:#f4f6f7;
    --teal:#3ea5a9;
    --teal-soft:#bfe2e2;
    --teal-pale:#e3f2f2;
    --ink:#7b7d80;
    --navy:#2c2f8c;
  }
  *{box-sizing:border-box;margin:0;padding:0}
  html,body{width:1200px;height:898px;overflow:hidden}
  body{background:var(--backdrop);font-family:"Lato",sans-serif;color:var(--ink);position:relative}

  .flyer{position:absolute;width:535px;background:var(--paper);overflow:hidden;
    box-shadow:0 3px 10px rgba(0,0,0,.18)}
  .flyer--front{left:43px;top:40px;height:743px}
  .flyer--back{left:628px;top:107px;height:745px}

  .corner-wash{position:absolute;left:0;top:0;width:230px;height:110px;
    background:linear-gradient(160deg,var(--teal-soft) 0%,var(--teal-pale) 40%,rgba(255,255,255,0) 75%)}
  .bottom-wash{position:absolute;left:0;right:0;bottom:0;
    background:linear-gradient(180deg,rgba(255,255,255,0) 0%,var(--teal-pale) 55%,#eef6f6 100%)}

  .brand{position:absolute;display:flex;align-items:center;gap:12px}
  .brand__dot{border-radius:50%;background:var(--navy);flex:none}
  .brand__name{font-weight:700;color:var(--navy);line-height:1.08}

  .front-brand{left:252px;top:42px}
  .front-brand .brand__dot{width:38px;height:38px}
  .front-brand .brand__name{font-size:30px}

  .back-brand{left:182px;top:560px}
  .back-brand .brand__dot{width:28px;height:28px}
  .back-brand .brand__name{font-size:22px}

  .overview-band{position:absolute;left:0;top:110px;width:255px;height:38px;
    background:linear-gradient(90deg,var(--paper-tint),rgba(244,246,247,0))}
  .overview-title{position:absolute;left:32px;top:120px;font-size:17px;font-weight:300;color:var(--ink)}
  .overview-text{position:absolute;left:30px;top:164px;width:490px;font-size:14.2px;line-height:24.5px;font-weight:300;color:var(--ink);white-space:nowrap}

  .photo{position:absolute}
  .front-photo{left:0;top:245px;width:535px;height:305px;
    background:linear-gradient(120deg,#d7c9b6 0%,#e9edf1 35%,#8ea9c8 55%,#f1ece6 80%,#ffffff 100%);
    clip-path:polygon(0 0,100% 0,100% 95%,88% 84%,70% 78%,45% 86%,28% 100%,0 100%)}

  .perks{position:absolute;left:37px;top:580px;list-style:none}
  .perks li,.services li,.conditions li{display:flex;align-items:center;font-weight:300}
  .perks li{font-size:15px;height:26px;color:var(--ink)}
  .tri{width:0;height:0;border-top:5.5px solid transparent;border-bottom:5.5px solid transparent;
    border-left:9px solid var(--teal);margin-right:9px;flex:none}

  .providers-note{position:absolute;right:27px;top:667px;text-align:right;font-size:12.5px;line-height:16px;color:var(--teal)}

  .contact-bar{position:absolute;height:24px;background:var(--teal);color:#fff;
    display:flex;align-items:center;justify-content:center;gap:10px;
    clip-path:polygon(2% 0,100% 0,98% 100%,0 100%)}
  .contact-bar__text{font-size:13px}
  .contact-bar__phone{font-size:17px;display:flex;align-items:center;gap:8px}
  .flyer--front .contact-bar{left:19px;top:710px;width:491px}
  .flyer--back .contact-bar{left:22px;top:708px;width:490px}

  .back-photo{left:323px;width:194px;height:133px}
  .back-photo--one{top:17px;background:linear-gradient(135deg,#a88f74,#e3c7a6 50%,#d98a3a)}
  .back-photo--two{top:168px;background:linear-gradient(135deg,#7e91a9,#e6cfb5 50%,#c7b9a2)}
  .back-photo--three{top:321px;background:linear-gradient(135deg,#c79a63,#9ba6b1 50%,#6d7c8c)}

  .section-title{color:var(--teal);font-weight:300}
  .services-title{position:absolute;left:41px;top:84px;font-size:17px}
  .services{position:absolute;left:39px;top:112px;list-style:none}
  .services li{font-size:15.5px;height:22px;color:var(--ink)}

  .populations-title{position:absolute;left:60px;top:256px;width:220px;text-align:center;line-height:17px}
  .populations-title span{display:block;font-size:17px}
  .populations-title small{display:block;font-size:13.5px}
  .populations-group{position:absolute;left:46px;top:298px;font-size:14.5px;color:var(--teal);font-weight:300}
  .conditions{position:absolute;left:46px;top:316px;list-style:none}
  .conditions li{font-size:13.5px;height:19.7px;color:var(--ink)}
  .conditions .tri{border-top-width:5px;border-bottom-width:5px;border-left-width:8px;margin-right:8px}

  .team{position:absolute;left:44px;top:470px;color:var(--teal);font-size:12.5px;line-height:16px}
  .team__label{margin-bottom:5px}

  .address-block{position:absolute;left:0;width:100%;top:654px;text-align:center;color:var(--teal);font-weight:300;font-size:18px;line-height:23px;font-style:normal}
  .address-block .sep{margin:0 12px}
</style>
</head>
<body>

<section class="flyer flyer--front" aria-label="Practice overview flyer">
  <div class="corner-wash"></div>
  <div class="bottom-wash" style="height:250px"></div>

  <div class="brand front-brand">
    <span class="brand__dot"></span>
    <span class="brand__name">Harbor Family<br>Wellness Clinic</span>
  </div>

  <div class="overview-band"></div>
  <h2 class="overview-title">Brief Overview of Practice:</h2>
  <p class="overview-text">A multi-disciplinary outpatient behavioral health practice providing comprehen-<br>sive evaluation, medication management, and ongoing therapy for both pediat-<br>ric and adult patients.&nbsp; Flexible Scheduling, including after school appointments.</p>

  <div class="photo front-photo" role="img" aria-label="Photo of a clinician meeting with a smiling father, mother and young daughter at a desk"></div>

  <ul class="perks">
    <li><span class="tri"></span>Most Pediatric Medicaid plans accepted</li>
    <li><span class="tri"></span>Many private insurance plans accepted (Adult &amp; Pediatric)</li>
    <li><span class="tri"></span>Reasonable self-pay rates</li>
  </ul>

  <p class="providers-note">Individuals associated with practice<br>Daniel R. Whitford, Ph.D.</p>

  <div class="contact-bar">
    <span class="contact-bar__text">Contact us today for a free, no obligation consultation:</span>
    <span class="contact-bar__phone">
      <svg width="14" height="14" viewBox="0 0 24 24" aria-hidden="true"><path fill="#fff" d="M6.6 10.8a15.1 15.1 0 0 0 6.6 6.6l2.2-2.2c.3-.3.7-.4 1-.2 1.1.4 2.3.6 3.6.6.6 0 1 .4 1 1V20c0 .6-.4 1-1 1A17 17 0 0 1 3 4c0-.6.4-1 1-1h3.5c.6 0 1 .4 1 1 0 1.3.2 2.5.6 3.6.1.3 0 .7-.2 1z"/></svg>
      555-310-4820
    </span>
  </div>
</section>

<section class="flyer flyer--back" aria-label="Services and contact flyer">
  <div class="corner-wash"></div>
  <div class="bottom-wash" style="height:270px"></div>

  <div class="photo back-photo back-photo--one" role="img" aria-label="Photo of a smiling schoolgirl writing at her desk in a classroom"></div>
  <div class="photo back-photo back-photo--two" role="img" aria-label="Photo of smiling teenage students seated in a classroom"></div>
  <div class="photo back-photo back-photo--three" role="img" aria-label="Photo of a young boy seated at a classroom desk"></div>

  <h2 class="section-title services-title">Specific Services Offered:</h2>
  <ul class="services">
    <li><span class="tri"></span>Neuropsychological Assessment</li>
    <li><span class="tri"></span>Psychological Assessment</li>
    <li><span class="tri"></span>Medication Management</li>
    <li><span class="tri"></span>Individual Therapy</li>
    <li><span class="tri"></span>Diagnostic Services</li>
  </ul>

  <h2 class="section-title populations-title"><span>Patient Populations Seen</span><small>(Treatment offered for):</small></h2>
  <p class="populations-group">Pediatric &amp; Adult</p>
  <ul class="conditions">
    <li><span class="tri"></span>Depression</li>
    <li><span class="tri"></span>Attention Deficit Hyperactivity Disorder</li>
    <li><span class="tri"></span>Autism</li>
    <li><span class="tri"></span>Post-Traumatic Stress Disorder</li>
    <li><span class="tri"></span>Bi Polar</li>
    <li><span class="tri"></span>Anxiety and Depression</li>
    <li><span class="tri"></span>Neurological Conditions</li>
  </ul>

  <div class="team">
    <p class="team__label">List of Individuals associated with practice</p>
    <p>Daniel R. Whitford, Ph.D.<br>Laura Kessen, Ph.D.<br>Renee Ostrander, MHNP<br>Marisol Vega, CPNP</p>
  </div>

  <div class="brand back-brand">
    <span class="brand__dot"></span>
    <span class="brand__name">Harbor Family<br>Wellness Clinic</span>
  </div>

  <address class="address-block">
    Tel 555-310-4820<span class="sep">|</span>Fax 555-310-482<br>
    2210 Willow Bend Road Suite A Fairhaven, LA 70400
  </address>

  <div class="contact-bar">
    <span class="contact-bar__text">Contact us today for a free, no obligation consultation:</span>
    <span class="contact-bar__phone">
      <svg width="14" height="14" viewBox="0 0 24 24" aria-hidden="true"><path fill="#fff" d="M6.6 10.8a15.1 15.1 0 0 0 6.6 6.6l2.2-2.2c.3-.3.7-.4 1-.2 1.1.4 2.3.6 3.6.6.6 0 1 .4 1 1V20c0 .6-.4 1-1 1A17 17 0 0 1 3 4c0-.6.4-1 1-1h3.5c.6 0 1 .4 1 1 0 1.3.2 2.5.6 3.6.1.3 0 .7-.2 1z"/></svg>
      555-310-4820
    </span>
  </div>
</section>

</body>
</html>
```